Stationery Design for Information Technology Company
Stationery Design
Stationery Design for Information Technology Company - Information Technology
Creative Brief
Professional
Arun Mehta
Director
58 Pell Road East, Suite 240 Ashford Glen, NJ 08917
kamal@greyoaksys.com
www.greyoaksys.com
Please use the Ai file uploaded BUT WITHOUT THE TAGLINE
On the card only mention "GREY OAK LOGO" NO NEED FOR "SOFTWARE SERVICES" I want the logo displayed on the front and back of the card with a back ground color that goes along with the logo design. I want the logo to be centrally located at the back of the card. THE LOGO SHOULD BE ON FRONT AND BACK. ON THE BACK IT SHOULD BE A FULL LOGO, WITH MY THREE OFFICES 1) USA 2)INDIA 3) AUSTRALIA

```html
<!DOCTYPE html>
<html lang="en">
<head>
<meta charset="utf-8">
<title>Grey Oak Stationery</title>
<link href="https://fonts.googleapis.com/css2?family=Open+Sans:wght@400;700&display=swap" rel="stylesheet">
<style>
  :root{
    --frame:#1e5e93;
    --board:#c9c7c7;
    --paper:#ffffff;
    --brand:#1f5a8e;
    --wave-grey:#7c7c7e;
    --ink:#4a4a4a;
    --name:#24486e;
  }
  *{margin:0;padding:0;box-sizing:border-box}
  html,body{width:1200px;height:954px;overflow:hidden}
  body{background:var(--frame);font-family:"Open Sans",Arial,sans-serif;color:var(--ink);position:relative}
  .board{position:absolute;left:20px;top:20px;width:1160px;height:914px;background:var(--board)}
  .wordmark{font-family:"Open Sans",Arial,sans-serif;font-weight:700;color:var(--name);letter-spacing:0.02em;white-space:nowrap}
  .board-mark{position:absolute;left:890px;top:52px;font-size:38px}
  .item{position:absolute;background:var(--paper);box-shadow:2px 3px 6px rgba(0,0,0,.28);overflow:hidden}
  .item svg.wave{position:absolute;left:0;bottom:0;display:block}
  .small{font-size:5.5px;line-height:8px;color:var(--ink);white-space:nowrap}
  .small b{font-weight:700;color:var(--name)}

  .letterhead{left:62px;top:116px;width:450px;height:582px}
  .letterhead .cols{position:absolute;left:14px;top:14px;display:flex;gap:44px}
  .letterhead .mark{position:absolute;right:28px;top:50px;font-size:22px}

  .sleeve{left:551px;top:150px;width:310px;height:315px}
  .sleeve .mark{position:absolute;left:78px;top:126px;font-size:18px}
  .sleeve .notch{position:absolute;right:-24px;top:132px;width:48px;height:48px;border-radius:50%;background:var(--board)}

  .disc{position:absolute;left:854px;top:153px;width:320px;height:320px;border-radius:50%;box-shadow:2px 3px 7px rgba(0,0,0,.3);overflow:hidden;background:var(--paper)}
  .disc .mark{position:absolute;left:100px;top:68px;font-size:20px}
  .disc .hub{position:absolute;left:124px;top:124px;width:72px;height:72px;border-radius:50%;background:#e7e7e7;border:1px solid #b9b9b9}
  .disc .hole{position:absolute;left:146px;top:146px;width:28px;height:28px;border-radius:50%;background:var(--board);border:1px solid #9a9a9a}

  .envelope{left:613px;top:590px;width:527px;height:302px}
  .envelope .flap{position:absolute;left:0;top:0;width:100%;height:88px;background:var(--frame)}
  .envelope .cols{position:absolute;left:12px;top:104px;display:flex;gap:48px}
  .envelope .mark{position:absolute;right:32px;top:120px;font-size:20px}

  .card{top:768px;width:251px;height:124px}
  .card-front{left:72px}
  .card-back{left:344px}
  .card .mark{position:absolute;left:14px;top:14px;font-size:15px}
  .card-front .title{position:absolute;right:12px;bottom:12px;text-align:right;color:#fff;font-size:5.5px;line-height:8px}
  .card-back .cols{position:absolute;left:14px;top:40px;display:flex;gap:26px}
</style>
</head>
<body>
<main class="board">
  <div class="wordmark board-mark">GREY OAK</div>
</main>

<section class="item letterhead" aria-label="Letterhead">
  <div class="cols small">
    <div><b>USA</b><br>58 Pell Road East, Suite 240<br>Ashford Glen, NJ 08917<br>Tel +1 732 555 0142<br>kamal@greyoaksys.com</div>
    <div><b>India</b><br>14 Lake View Road<br>Pune 411001<br>Tel +91 20 5550 1188<br>www.greyoaksys.com</div>
    <div><b>Australia</b><br>9 Harbour Street<br>Sydney NSW 2000<br>Tel +61 2 5550 7731</div>
  </div>
  <div class="wordmark mark">GREY OAK</div>
  <svg class="wave" width="450" height="582" viewBox="0 0 450 582">
    <path d="M0,548 Q230,480 450,352 L450,364 Q230,494 0,556Z" fill="var(--brand)"/>
    <path d="M0,560 Q230,498 450,372 L450,582 L0,582Z" fill="var(--wave-grey)"/>
  </svg>
</section>

<section class="item sleeve" aria-label="CD sleeve">
  <div class="wordmark mark">GREY OAK</div>
  <svg class="wave" width="310" height="315" viewBox="0 0 310 315">
    <path d="M0,292 Q150,262 310,190 L310,200 Q150,274 0,300Z" fill="var(--brand)"/>
    <path d="M0,304 Q150,280 310,206 L310,315 L0,315Z" fill="var(--wave-grey)"/>
  </svg>
  <div class="notch"></div>
</section>

<section class="disc" aria-label="CD label">
  <svg class="wave" width="320" height="320" viewBox="0 0 320 320">
    <path d="M0,122 Q170,150 320,96 L320,110 Q170,166 0,136Z" fill="var(--brand)"/>
    <path d="M0,140 Q170,172 320,114 L320,320 L0,320Z" fill="var(--wave-grey)"/>
  </svg>
  <div class="wordmark mark">GREY OAK</div>
  <div class="hub"></div>
  <div class="hole"></div>
</section>

<section class="item envelope" aria-label="Envelope">
  <div class="flap"></div>
  <div class="cols small">
    <div><b>USA</b><br>58 Pell Road East, Suite 240<br>Ashford Glen, NJ 08917<br>Tel +1 732 555 0142<br>kamal@greyoaksys.com</div>
    <div><b>India</b><br>14 Lake View Road<br>Pune 411001<br>Tel +91 20 5550 1188</div>
    <div><b>Australia</b><br>9 Harbour Street<br>Sydney NSW 2000<br>www.greyoaksys.com</div>
  </div>
  <div class="wordmark mark">GREY OAK</div>
  <svg class="wave" width="527" height="302" viewBox="0 0 527 302">
    <path d="M0,286 Q270,276 527,226 L527,234 Q270,286 0,292Z" fill="var(--brand)"/>
    <path d="M0,296 Q270,292 527,240 L527,302 L0,302Z" fill="var(--wave-grey)"/>
  </svg>
</section>

<section class="item card card-front" aria-label="Business card front">
  <div class="wordmark mark">GREY OAK</div>
  <svg class="wave" width="251" height="124" viewBox="0 0 251 124">
    <path d="M0,96 Q120,90 251,52 L251,60 Q120,98 0,102Z" fill="var(--brand)"/>
    <path d="M0,106 Q120,102 251,66 L251,124 L0,124Z" fill="var(--wave-grey)"/>
  </svg>
  <div class="title">Arun Mehta<br>Director</div>
</section>

<section class="item card card-back" aria-label="Business card back">
  <div class="wordmark mark">GREY OAK</div>
  <div class="cols small">
    <div><b>Arun Mehta</b><br>Director<br>58 Pell Road East, Suite 240<br>Ashford Glen, NJ 08917<br>kamal@greyoaksys.com</div>
    <div><b>India</b><br>Pune 411001<br><b>Australia</b><br>Sydney NSW 2000<br>www.greyoaksys.com</div>
  </div>
  <svg class="wave" width="251" height="124" viewBox="0 0 251 124">
    <path d="M0,104 Q120,100 251,66 L251,73 Q120,108 0,110Z" fill="var(--brand)"/>
    <path d="M0,113 Q120,112 251,78 L251,124 L0,124Z" fill="var(--wave-grey)"/>
  </svg>
</section>
</body>
</html>
```